Etiketten für Ätherische Öle, Extrakte und Speiseöle gesucht
Zielgruppe
Wir verkaufen natürlich Produkte. Ätherische öle, Extrakte, Speise öle.
Wir verkaufen im Webshop, Kaufwelt und auch im Betrieb.
https://www.natur-sefo.com
Wir verkaufen hauptsächlich innerhalb Italiens und Deutschland daher doppel sprachig.
Aufgabenstellung
Guten Tag
Bitte verwenden Sie! : * beispiel_10_ml_etikett_nachbau.jpg *
Da mir die kleinste Größe die wichtigste ist habe ich ein beispiel Hochgeladen. Das kleinste Etikett lässt sich öffnen und daher sind nur 7 cm ersichtlich und man muss das Etikett aufmachen.
Habe ein Beispiel Hochgeladen. Aber bitte einfach kreativ sein. *Anhang: beispiel Etikett*
Sobald ich eine Art vom kelinsten habe würde ich dies für die 2 anderen Größen übernehmen aber das man Sie irgendwie gut unterscheiden kann da dies dann komplett andere Produkte (Extrakte/Speise öl) sein werden.
Erstellung von drei unterschiedlichen Größen von Etiketten mit folgenden Eigenschaften:
Am wichtigsten ist mir das kleinste Etikett da dies auch am schwersten ist daher habe ich die anderen Größen nun gelöscht!
• 10 ml Länge: 155 mm Breite: 32 mm.
Brauche 3 unterschiedliche Grund Farben: z. B. Ätherische Öle (Grün) Extrakte (Rot) Speiseöle (gelb). Die Farben lasse ich sie entscheiden.
Die Etiketten müssen 2 Sprachen (Deutsch / Italienisch) sein deshalb muss dieses berücksichtigt werden.
Anbei finden Sie:
• Logo (Bild Logo)
• Beispiel Text ätherische Öle
• Bilder der aktuellen Flaschen
Unter https://www.natur-sefo.com/de finden Sie meine Seite
Anmerkung: Im Anhang: *Back*
Habe ich mein Logo mit Firmennamen ; Bio des Hollmer Tobias
Da ich jedoch nicht alle Produkte im biologischen Anbau habe und mein Logo zu miss Verständnis führen könnte habe ich ein Bildliches Logo gemacht das ich fortan auf meinen Produkten haben möchte. Im besonderes dieses Grün das in beiden vorhanden ist versuche ich zu integrieren.
Habe selbst ein Etikett designet das aber sehr unprofessionell wirkt aber dieses Grüne das ich gerne als merkmal unterbringen würde.
Siehe Anhang: neemöl

```html
<!DOCTYPE html>
<html lang="de">
<head>
<meta charset="utf-8">
<title>Lavanda Vera – Etikett 30 ml</title>
<link rel="stylesheet" href="https://fonts.googleapis.com/css2?family=Nunito+Sans:wght@400;700&family=Great+Vibes&family=Montserrat:wght@300&display=swap">
<style>
  :root {
    --page: #ffffff;
    --label-green: #9bb46c;
    --panel-green: #b3c78f;
    --frame-pink: #e5246b;
    --text-blue: #2f3d96;
    --text-white: #ffffff;
    --band-red: #8a0000;
    --art-petal: #c9b8c4;
    --art-leaf: #a9cc4a;
  }
  * { margin: 0; padding: 0; box-sizing: border-box; }
  html, body { width: 1200px; height: 461px; overflow: hidden; background: var(--page); }
  body { font-family: "Nunito Sans", Arial, sans-serif; }

  .label {
    position: relative; width: 1200px; height: 461px;
  }
  .label__base {
    position: absolute; left: 47px; top: 37px; width: 1112px; height: 385px;
    background: var(--label-green);
  }
  .label__front {
    position: absolute; left: 448px; top: 42px; width: 389px; height: 372px;
    background: var(--panel-green);
    overflow: hidden;
  }
  .label__art {
    position: absolute; inset: 0;
    background:
      radial-gradient(ellipse 60% 45% at 50% 38%, var(--art-petal) 0%, rgba(201,184,196,0.4) 45%, transparent 75%),
      radial-gradient(ellipse 90% 40% at 70% 100%, var(--art-leaf) 0%, transparent 70%);
    opacity: 0.85;
  }
  .label__cutline {
    position: absolute; left: 58px; top: 47px; width: 1090px; height: 364px;
    border: 2px solid var(--frame-pink);
    pointer-events: none;
  }

  .usage {
    position: absolute; left: 69px; top: 73px; width: 330px;
    color: var(--text-blue); font-size: 14.5px; line-height: 17.5px;
  }
  .usage strong { font-weight: 700; }

  .company {
    position: absolute; left: 70px; top: 252px; width: 360px;
    color: var(--text-white); font-size: 14.5px; line-height: 15.5px;
  }
  .company__title { font-weight: 700; }

  .product-name {
    position: absolute; left: 448px; top: 168px; width: 389px; text-align: center;
    font-family: "Great Vibes", cursive; color: var(--text-white);
    font-size: 70px; line-height: 1;
  }
  .product-variety {
    position: absolute; left: 600px; top: 258px;
    font-family: "Montserrat", sans-serif; font-weight: 300;
    color: var(--text-white); font-size: 18px; letter-spacing: 12px;
  }
  .volume {
    position: absolute; left: 448px; top: 333px; width: 389px; height: 31px;
    background: var(--band-red); color: var(--text-white);
    font-size: 20px; line-height: 31px; text-align: center;
  }

  .warnings {
    position: absolute; left: 886px; top: 76px; width: 262px;
    color: var(--text-blue); font-size: 16.5px; line-height: 17px;
  }
  .origin {
    position: absolute; left: 886px; top: 259px;
    color: var(--text-white); font-size: 17.5px;
  }
  .lot {
    position: absolute; left: 888px; top: 286px;
    color: var(--text-white); font-size: 12px; font-weight: 700;
  }
  .best-before {
    position: absolute; left: 889px; top: 313px;
    color: var(--text-white); font-size: 11px;
  }
  .best-before__field {
    position: absolute; left: 888px; top: 328px; width: 240px; height: 66px;
    background: var(--text-white);
  }
</style>
</head>
<body>
<main class="label">
  <div class="label__base"></div>

  <section class="label__front">
    <div class="label__art" role="img" aria-label="Aquarell-Illustration einer violetten Blüte mit grünen Blättern"></div>
  </section>

  <p class="usage">
    100% natürliches etherisches Öl.<br>
    Aroma-Kosmetikum zur Körperpflege.<br>
    <strong>Anwendung:</strong> Als Haut- u. Massageöl<br>
    max 15 Tr. Mit 50 ml z.B. Mandelöl<br>
    mischen.<br>
    Als Badezusatz 8-15 Tr. Auf 4 Eßl. Sahne<br>
    oder Milch ins Badewasser geben.
  </p>

  <address class="company" style="font-style: normal;">
    <span class="company__title">Firmenname:</span><br>
    Bio des Hollmer Tobias<br>
    Lindenweg 8<br>
    I-39020 Talfeld<br>
    IVA: IT04518260935<br>
    CF.: HLLTBS88M12B402K<br>
    Tel; +39 0471/284617 Handy; 3406128853<br>
    https://www.natur-sefo.com/<br>
    Info.natursefo@mail.com
  </address>

  <h1 class="product-name" style="font-weight: 400;">Lavanda</h1>
  <p class="product-variety">Vera</p>
  <p class="volume">30 ml</p>

  <p class="warnings">
    Nur in der angegeben Ver-<br>
    dünnung anwenden!<br>
    Nicht in die Augen oder auf<br>
    die Schleimhäute<br>
    bringen!<br>
    Außer Reichweite von Kindern<br>
    lagern.
  </p>

  <p class="origin">Abgefüllt in Italien</p>
  <p class="lot">LottoNummer/CH nummer: 123456</p>
  <p class="best-before">Mindestens haltbar bis:</p>
  <div class="best-before__field"></div>

  <div class="label__cutline"></div>
</main>
</body>
</html>
```